Website for Corvalind Capital, my new firm that raises money from investors to buy, build, own an...

Corvalind Capital needs a website! We are a new company with very experienced people, who invest in, own and build hotel properties, as well as apartments and other commercial real estate. We seek investors for our projects, and we provide safe, secure returns on their investment in our projects. Our new logo is designed to exhibit strength, class and security, and would like our website to continue on this theme. Our name, Corvalind, is a word-play on a Greek word “aristeia”, which means “excellence” and “a warriors finest moment of glory in war”. If you are in business, you realize that much of it is like war, with strategy and moves and opponents and competitors, and ever-changing economic conditions and threats that make business very much like war. We like to think that we are good at business (war), and so have named our company “Corvalind”, using the founders last name and the word “aristeia” combined. Another definition of "aristeia" is "performing at the peak of one's potential after a long struggle"...again, much like business in real life! The website design should exhibit financial security, smart moves, and positive growth towards a bright future.

Target Market(s)

The target market is smart and wealthy investors, with others such as brokers, cities and government agencies, lenders, sellers, partners, etc also looking at it.

Industry/Entity Type

Investment

Number of Pages Required

5+ page

Font styles to use
Sans Serif

Colors
fec214

Requirements
Must have
• Our website should have a landing page, a "about" or bio page, a projects page and a contact us page. Our new logo uses the colors black and gold, so this should be factored in to our site. The site should be simple, yet impactful and impressive. I have actually two logos, which can be mixed and interchanged in a complimentary way, each with their own unique look.
Nice to have
• I have uploaded a couple screenshots of a website i like, and the simplicity I mention.
Should not have
• The site should not be flashy or complicated or complex or "busy"

```html
<!DOCTYPE html>
<html lang="en">
<head>
<meta charset="utf-8">
<title>Corvalind Capital</title>
<link href="https://fonts.googleapis.com/css2?family=Montserrat:wght@400;600;700;800&family=Quicksand:wght@400;500;600;700&display=swap" rel="stylesheet">
<style>
:root{
  --gold:#fec214;
  --ink:#1e1e1e;
  --dark:#2b2d30;
  --footer:#3a3a3a;
  --muted:#666;
  --line:#e3e3e3;
  --white:#fff;
}
*{box-sizing:border-box;margin:0;padding:0}
html,body{width:1200px;height:5000px;overflow:hidden}
body{position:relative;background:var(--white);font-family:"Quicksand",sans-serif;color:var(--ink)}
.abs{position:absolute}
.head-font{font-family:"Montserrat",sans-serif}

/* hero */
.hero{left:0;top:0;width:1200px;height:720px;background:linear-gradient(180deg,#5b8fd6 0%,#9cc1ea 35%,#8a7a66 62%,#6d8a44 82%,#4e6b2e 100%)}
.brand{left:18px;top:14px;display:flex;flex-direction:column;align-items:center;width:170px}
.brand-mark{width:56px;height:56px;border:4px solid var(--gold);border-radius:50%}
.brand-name{font-family:"Montserrat",sans-serif;font-weight:700;color:var(--gold);font-size:22px;letter-spacing:2px;margin-top:6px}
.nav{left:200px;top:40px;display:flex;gap:0}
.nav a{font-family:"Montserrat",sans-serif;color:#fff;font-size:17px;font-weight:600;text-decoration:none;padding:10px 36px;display:block}
.nav a.active{background:var(--gold)}
.hero-box{left:310px;top:215px;width:390px;height:175px;background:rgba(40,40,40,.55);padding:14px 18px}
.hero-box h1{font-family:"Montserrat",sans-serif;color:var(--gold);font-size:32px;font-weight:800;letter-spacing:1px}
.hero-box p{color:#fff;font-size:13px;line-height:1.35;margin-top:6px}
.hero-price{left:305px;top:405px;display:flex;align-items:center;gap:14px}
.hero-price .amt{font-family:"Montserrat",sans-serif;color:#fff;font-weight:800;font-size:38px}
.hero-price .more{background:var(--gold);color:#fff;font-family:"Montserrat",sans-serif;font-weight:700;font-size:30px;padding:4px 18px;margin-left:20px}

.search{left:73px;top:625px;width:1044px;height:125px;background:var(--gold);display:flex;align-items:center;padding:0 35px;gap:14px}
.search .field{background:#fff;height:50px;display:flex;align-items:center;justify-content:center;font-size:15px;font-weight:600;color:#333}
.search .street{width:380px}
.search .city{width:222px}
.search .state{width:222px}
.search .go{width:112px;background:var(--ink);color:#fff}

/* services */
.service{top:855px;width:345px;height:380px;border:2px solid var(--line);background:#fff;text-align:center;padding:0 18px}
.service .icon{width:110px;height:110px;border-radius:50%;border:6px solid var(--gold);background:#fff;margin:-24px auto 0;display:flex;align-items:center;justify-content:center}
.service h3{font-family:"Montserrat",sans-serif;font-weight:800;font-size:26px;margin-top:10px}
.service p{font-size:14px;line-height:1.3;text-align:left;margin-top:8px;color:#222}
.service .btn{position:absolute;bottom:0;left:50%;transform:translateX(-50%);background:var(--gold);font-family:"Montserrat",sans-serif;font-weight:700;font-size:15px;padding:11px 26px;width:170px}

.section-title{left:0;width:1200px;text-align:center;font-family:"Montserrat",sans-serif;font-weight:800;font-size:42px;letter-spacing:1px}

/* recent */
.prop{width:505px;height:302px}
.prop .tag{position:absolute;left:26px;top:22px;background:var(--gold);font-family:"Montserrat",sans-serif;font-weight:600;font-size:15px;padding:10px 24px}
.prop .addr{position:absolute;left:30px;bottom:40px;color:#fff;font-size:15px;font-weight:600;display:flex;gap:8px;align-items:center}
.prop .price{position:absolute;right:18px;bottom:32px;background:var(--ink);color:#fff;font-weight:700;font-size:16px;padding:8px 14px}
.view-more{left:1020px;top:2088px;background:var(--gold);font-family:"Montserrat",sans-serif;font-weight:700;font-size:16px;padding:12px 20px}

/* team */
.team{left:0;top:2167px;width:1200px;height:385px;background:linear-gradient(180deg,#2d3646,#454c57 60%,#2a2d33)}
.team h2{font-family:"Montserrat",sans-serif;color:#fff;font-weight:700;font-size:42px;text-align:center;margin-top:28px}
.team .sub{color:#fff;text-align:center;font-size:16px}
.member{top:2285px;width:210px;height:230px;background:#fff;padding:10px 10px 0}
.member .photo{height:150px;background:linear-gradient(160deg,#cfcfcf,#8a8a8a)}
.member .name{font-family:"Montserrat",sans-serif;font-weight:700;font-size:14px;margin-top:12px}
.member .role{font-size:12px;color:#555}
.member .soc{position:absolute;right:12px;top:138px;width:36px;height:36px;background:var(--gold)}
.dots{left:560px;top:2602px;display:flex;gap:8px}
.dots span{width:8px;height:8px;border-radius:50%;background:#bbb}
.dots span.on{background:#666}

/* featured */
.tabs{left:0;top:2755px;width:1200px;display:flex;justify-content:center;gap:46px;font-weight:700;font-size:16px}
.tabs .active{border-bottom:3px solid var(--gold);padding-bottom:4px}
.listing{width:330px;height:540px;border:1px solid var(--line);background:#fff}
.listing .photo{height:222px}
.listing h4{font-family:"Montserrat",sans-serif;font-weight:800;font-size:16px;padding:14px 16px 6px}
.listing .loc{padding:0 16px;font-size:15px;font-weight:700;display:flex;gap:8px;align-items:center}
.listing .facts{display:grid;grid-template-columns:1fr 1fr;gap:18px 8px;padding:22px 16px 0;font-size:14px;font-weight:500}
.listing .facts span{display:flex;align-items:center;gap:8px}
.listing .facts i{width:14px;height:14px;background:var(--gold);border-radius:2px;display:inline-block}
.listing .price{position:absolute;left:0;bottom:0;width:100%;height:70px;background:var(--gold);font-family:"Montserrat",sans-serif;font-weight:800;font-size:38px;text-align:center;line-height:70px}

/* clients */
.clients{left:0;top:3993px;width:1200px;height:480px;background:linear-gradient(180deg,#1f2228,#3a3f46 50%,#2f4a2e)}
.clients h2{font-family:"Montserrat",sans-serif;color:#fff;font-weight:700;font-size:42px;text-align:center;margin-top:40px}
.client-photo{left:73px;top:4110px;width:200px;height:200px;background:linear-gradient(160deg,#ddd,#888);border:6px solid #fff}
.client-quote{left:300px;top:4150px;width:830px;color:#fff;font-size:17px;line-height:1.35}
.client-name{left:920px;top:4330px;width:230px;text-align:right;color:#fff}
.client-name b{font-family:"Montserrat",sans-serif;font-size:22px;display:block}

/* partners */
.partners{left:56px;top:4517px;width:1094px;height:165px;background:var(--gold);border-radius:6px;display:flex;align-items:center;justify-content:space-around}
.partners span{font-family:"Montserrat",sans-serif;font-weight:800;font-size:46px;color:var(--ink);display:flex;align-items:center;gap:12px}
.partners span i{width:36px;height:36px;background:var(--ink);display:inline-block}

/* footer */
.footer{left:0;top:4700px;width:1200px;height:300px;background:var(--footer);color:#fff}
.footer h5{font-family:"Montserrat",sans-serif;font-weight:700;font-size:18px;margin-bottom:16px}
.footer .col{position:absolute;top:40px;font-size:13px}
.footer .col li{list-style:none;margin-bottom:12px;display:flex;gap:10px;align-items:center}
.footer .col li i{width:12px;height:12px;background:#ddd;display:inline-block;border-radius:2px}
.places{display:grid;grid-template-columns:105px 105px;gap:8px 0}
.news-input{display:flex;margin-top:14px}
.news-input span{background:#fff;color:#777;width:200px;height:36px;font-size:12px;padding:10px}
.news-input b{background:var(--gold);width:60px;height:36px}
.socials{left:45px;top:200px;display:flex;gap:10px}
.socials i{width:26px;height:26px;background:#fff;display:inline-block}
.copy{left:0;bottom:0;width:1200px;text-align:center;font-size:12px;padding:10px;border-top:1px solid #555}
</style>
</head>
<body>

<section class="abs hero" role="img" aria-label="Photograph of a large stone two-storey house with lawn under a blue sky"></section>
<div class="abs brand">
  <div class="brand-mark"></div>
  <div class="brand-name">CORVALIND</div>
</div>
<nav class="abs nav">
  <a href="#">HOME</a><a href="#">ABOUT US</a><a href="#" class="active">GALLERY</a><a href="#">OUR SERVICE</a><a href="#">BLOG</a>
</nav>
<div class="abs hero-box">
  <h1>HEAVEN PALACE</h1>
  <p>Lorem Ipsum is simply dummy text of the printing and typesetting industry. Lorem Ipsum has been the industry's standard dummy text ever since the 1500s, when an unknown printer took a galley of type and scrambled it to make a type specimen book. It has survived not only five centuries, but also the leap into</p>
</div>
<div class="abs hero-price">
  <svg width="40" height="40" viewBox="0 0 24 24"><path d="M3 12V4h8l10 10-8 8z" fill="#fff"/><circle cx="7.5" cy="8" r="1.6" fill="#555"/></svg>
  <span class="amt">300, 000</span>
  <span class="more">More details</span>
  <svg width="40" height="40" viewBox="0 0 24 24"><path d="M4 12h14M12 5l7 7-7 7" stroke="#fff" stroke-width="3" fill="none"/></svg>
</div>

<div class="abs search">
  <div class="field street">Enter a street name or keyword</div>
  <div class="field city">City</div>
  <div class="field state">State</div>
  <div class="field go">Search</div>
</div>

<div class="abs service" style="left:45px">
  <div class="icon"><svg width="56" height="56" viewBox="0 0 24 24"><path d="M2 14l5-4 4 2 4-3 7 5-5 4-5-2-3 2z" fill="#1a8f88"/></svg></div>
  <h3>WANT TO BUY?</h3>
  <p>Lorem Ipsum is simply dummy text of the printing and typesetting industry. Lorem Ipsum has been the industry's standard dummy text ever since the 1500s, when an unknown printer took a galley of type and scrambled it to make a type specimen book. It has survived not only five centuries, but</p>
  <div class="btn">MORE DETAILS</div>
</div>
<div class="abs service" style="left:428px">
  <div class="icon"><svg width="56" height="56" viewBox="0 0 24 24"><rect x="4" y="6" width="7" height="16" fill="#1a8f88"/><rect x="13" y="2" width="7" height="20" fill="#2a3e6e"/></svg></div>
  <h3>WANT TO BUILD?</h3>
  <p>Lorem Ipsum is simply dummy text of the printing and typesetting industry. Lorem Ipsum has been the industry's standard dummy text ever since the 1500s, when an unknown printer took a galley of type and scrambled it to make a type specimen book. It has survived not only five centuries, but</p>
  <div class="btn">MORE DETAILS</div>
</div>
<div class="abs service" style="left:811px">
  <div class="icon"><svg width="56" height="56" viewBox="0 0 24 24"><rect x="4" y="4" width="16" height="8" fill="#1a8f88"/><circle cx="12" cy="15" r="5" fill="#2a3e6e"/><rect x="11" y="19" width="2" height="4" fill="#333"/></svg></div>
  <h3>WANT TO INVEST?</h3>
  <p>Lorem Ipsum is simply dummy text of the printing and typesetting industry. Lorem Ipsum has been the industry's standard dummy text ever since the 1500s, when an unknown printer took a galley of type and scrambled it to make a type specimen book. It has survived not only five centuries, but</p>
  <div class="btn">MORE DETAILS</div>
</div>

<h2 class="abs section-title" style="top:1290px">RECENT PROPERTIES</h2>

<div class="abs prop" style="left:73px;top:1407px;background:linear-gradient(120deg,#e8e8e8,#9fb4c8 55%,#5e8fd0)" role="img" aria-label="Photograph of a modern white apartment tower against blue sky">
  <span class="tag">For sell</span>
  <span class="addr"><svg width="14" height="18" viewBox="0 0 14 18"><path d="M7 0a7 7 0 0 0-7 7c0 5 7 11 7 11s7-6 7-11a7 7 0 0 0-7-7z" fill="var(--gold)"/></svg>142 Willowmere Dr Ashby</span>
  <span class="price">$1,777,000</span>
</div>
<div class="abs prop" style="left:610px;top:1407px;background:linear-gradient(180deg,#2c4d8e,#5d79b4 50%,#6b7a55 85%)" role="img" aria-label="Photograph of a two-storey house lit at dusk">
  <span class="tag">For rent</span>
  <span class="addr"><svg width="14" height="18" viewBox="0 0 14 18"><path d="M7 0a7 7 0 0 0-7 7c0 5 7 11 7 11s7-6 7-11a7 7 0 0 0-7-7z" fill="var(--gold)"/></svg>2405 Rowan Park Street</span>
  <span class="price">$1255/month</span>
</div>
<div class="abs prop" style="left:73px;top:1740px;background:linear-gradient(180deg,#a8c6e6,#b89a80 45%,#7d9a54 80%)" role="img" aria-label="Photograph of a brick family house with green lawn">
  <span class="tag">For sell</span>
  <span class="addr"><svg width="14" height="18" viewBox="0 0 14 18"><path d="M7 0a7 7 0 0 0-7 7c0 5 7 11 7 11s7-6 7-11a7 7 0 0 0-7-7z" fill="var(--gold)"/></svg>5820 Harbor Ave Apt 410</span>
  <span class="price">$150,000</span>
</div>
<div class="abs prop" style="left:610px;top:1740px;background:linear-gradient(180deg,#9ec0e4,#8b7a5e 45%,#6d8f3c 80%)" role="img" aria-label="Photograph of a ranch house with long driveway and trees">
  <span class="tag">For rent</span>
  <span class="addr"><svg width="14" height="18" viewBox="0 0 14 18"><path d="M7 0a7 7 0 0 0-7 7c0 5 7 11 7 11s7-6 7-11a7 7 0 0 0-7-7z" fill="var(--gold)"/></svg>318 N Elmcrest Dr Apt 207</span>
  <span class="price">$3000/month</span>
</div>
<div class="abs view-more">View more</div>

<section class="abs team" role="img" aria-label="Darkened photograph of a modern building at dusk">
  <h2>A humble Team we are</h2>
  <p class="sub">We'll some of us anyways</p>
</section>
<div class="abs member" style="left:120px;transform:rotate(-3deg)"><div class="photo" role="img" aria-label="Portrait photo of a team member"></div><div class="name">Owen Pratt</div><div class="role">Digital Producer</div><span class="soc"></span></div>
<div class="abs member" style="left:345px;transform:rotate(2deg)"><div class="photo" role="img" aria-label="Portrait photo of a team member"></div><div class="name">Lena Voss</div><div class="role">Designer</div><span class="soc"></span></div>
<div class="abs member" style="left:575px;transform:rotate(-2deg)"><div class="photo" role="img" aria-label="Portrait photo of a team member"></div><div class="name">Carl Mendez</div><div class="role">Developer</div><span class="soc"></span></div>
<div class="abs member" style="left:800px;transform:rotate(3deg)"><div class="photo" role="img" aria-label="Portrait photo of a team member"></div><div class="name">Ivo Tarrant</div><div class="role">Administration</div><span class="soc"></span></div>
<div class="abs dots"><span class="on"></span><span></span><span></span><span></span></div>

<h2 class="abs section-title" style="top:2672px">FEATURED LISTINGS</h2>
<div class="abs tabs"><span>All</span><span>Properties</span><span>Office</span><span class="active">Appertment</span><span>Land</span></div>

<div class="abs listing" style="left:57px;top:2828px"><div class="photo" style="background:linear-gradient(180deg,#8fb6e0,#b5a68a 50%,#6f9a45)" role="img" aria-label="Photograph of a single-storey house with lawn"></div><h4>1870 S LINDEN RIDGE BLVD</h4><div class="loc"><svg width="14" height="18" viewBox="0 0 14 18"><path d="M7 0a7 7 0 0 0-7 7c0 5 7 11 7 11s7-6 7-11a7 7 0 0 0-7-7z" fill="var(--gold)"/></svg>Fairhaven, CA 90512</div><div class="facts"><span><i></i>800 Square foot</span><span><i></i>2-Garages</span><span><i></i>10 Bedrooms</span><span><i></i>6 Bathrooms</span><span><i></i>Reid Calder</span><span><i></i>1 days ago</span></div><div class="price">$150,000</div></div>
<div class="abs listing" style="left:435px;top:2828px"><div class="photo" style="background:linear-gradient(180deg,#7a5434,#c9b089 50%,#5e7a3c)" role="img" aria-label="Photograph of a sunroom interior with wooden frames"></div><h4>1870 S LINDEN RIDGE BLVD</h4><div class="loc"><svg width="14" height="18" viewBox="0 0 14 18"><path d="M7 0a7 7 0 0 0-7 7c0 5 7 11 7 11s7-6 7-11a7 7 0 0 0-7-7z" fill="var(--gold)"/></svg>Fairhaven, CA 90512</div><div class="facts"><span><i></i>800 Square foot</span><span><i></i>2-Garages</span><span><i></i>10 Bedrooms</span><span><i></i>6 Bathrooms</span><span><i></i>Reid Calder</span><span><i></i>1 days ago</span></div><div class="price">$150,000</div></div>
<div class="abs listing" style="left:813px;top:2828px"><div class="photo" style="background:linear-gradient(180deg,#9cc0e6,#9a6a4e 50%,#6c8f40)" role="img" aria-label="Photograph of a red brick family house"></div><h4>1870 S LINDEN RIDGE BLVD</h4><div class="loc"><svg width="14" height="18" viewBox="0 0 14 18"><path d="M7 0a7 7 0 0 0-7 7c0 5 7 11 7 11s7-6 7-11a7 7 0 0 0-7-7z" fill="var(--gold)"/></svg>Fairhaven, CA 90512</div><div class="facts"><span><i></i>800 Square foot</span><span><i></i>2-Garages</span><span><i></i>10 Bedrooms</span><span><i></i>6 Bathrooms</span><span><i></i>Reid Calder</span><span><i></i>1 days ago</span></div><div class="price">$150,000</div></div>

<div class="abs listing" style="left:57px;top:3400px"><div class="photo" style="background:linear-gradient(180deg,#a6c6e8,#7a7f88 50%,#6a8c44)" role="img" aria-label="Photograph of a grey two-storey house"></div><h4>1870 S LINDEN RIDGE BLVD</h4><div class="loc"><svg width="14" height="18" viewBox="0 0 14 18"><path d="M7 0a7 7 0 0 0-7 7c0 5 7 11 7 11s7-6 7-11a7 7 0 0 0-7-7z" fill="var(--gold)"/></svg>Fairhaven, CA 90512</div><div class="facts"><span><i></i>800 Square foot</span><span><i></i>2-Garages</span><span><i></i>10 Bedrooms</span><span><i></i>6 Bathrooms</span><span><i></i>Reid Calder</span><span><i></i>1 days ago</span></div><div class="price">$150,000</div></div>
<div class="abs listing" style="left:435px;top:3400px"><div class="photo" style="background:linear-gradient(180deg,#6f9fdc,#e4e4e4 55%,#7a9a52)" role="img" aria-label="Photograph of a white colonial mansion with columns"></div><h4>1870 S LINDEN RIDGE BLVD</h4><div class="loc"><svg width="14" height="18" viewBox="0 0 14 18"><path d="M7 0a7 7 0 0 0-7 7c0 5 7 11 7 11s7-6 7-11a7 7 0 0 0-7-7z" fill="var(--gold)"/></svg>Fairhaven, CA 90512</div><div class="facts"><span><i></i>800 Square foot</span><span><i></i>2-Garages</span><span><i></i>10 Bedrooms</span><span><i></i>6 Bathrooms</span><span><i></i>Reid Calder</span><span><i></i>1 days ago</span></div><div class="price">$150,000</div></div>
<div class="abs listing" style="left:813px;top:3400px"><div class="photo" style="background:linear-gradient(180deg,#b4cfe9,#6e5a45 50%,#5c7a36)" role="img" aria-label="Photograph of a thatched-roof cottage"></div><h4>1870 S LINDEN RIDGE BLVD</h4><div class="loc"><svg width="14" height="18" viewBox="0 0 14 18"><path d="M7 0a7 7 0 0 0-7 7c0 5 7 11 7 11s7-6 7-11a7 7 0 0 0-7-7z" fill="var(--gold)"/></svg>Fairhaven, CA 90512</div><div class="facts"><span><i></i>800 Square foot</span><span><i></i>2-Garages</span><span><i></i>10 Bedrooms</span><span><i></i>6 Bathrooms</span><span><i></i>Reid Calder</span><span><i></i>1 days ago</span></div><div class="price">$150,000</div></div>

<section class="abs clients" role="img" aria-label="Darkened photograph of a house at night among trees">
  <h2>OUR HAPPY CLIENTS</h2>
</section>
<div class="abs client-photo" role="img" aria-label="Portrait photo of a client"></div>
<p class="abs client-quote">Lorem Ipsum is simply dummy text of the printing and typesetting industry. Lorem Ipsum has been the industry's standard dummy text ever since the 1500s, when an unknown printer took a galley of type and scrambled it to make a type specimen book. It has survived not only five centuries, but also the leap into electronic typesetting, remaining essentially unchanged. It was popularised in the 1960s with the release of Letraset sheets conta</p>
<div class="abs client-name"><b>MAREK HOLLIS</b>United State</div>

<div class="abs partners">
  <span>Brightlens</span>
  <span><i></i>Siteward</span>
  <span>ledgerpoint</span>
  <span>marrowind</span>
</div>

<footer class="abs footer">
  <div class="abs brand" style="left:30px;top:40px">
    <div class="brand-mark"></div>
    <div class="brand-name">CORVALIND</div>
  </div>
  <div class="abs socials"><i></i><i></i><i></i><i></i></div>
  <div class="col" style="left:265px">
    <h5>CONTACT WITH US</h5>
    <ul>
      <li><i></i>418 Harrow Lane Suite 12, Fairhaven, CA</li>
      <li><i></i>(+1) 555 014 2290</li>
      <li><i></i>info@corvalind.example</li>
      <li><i></i>Mon - Sat, 08 AM - 06 PM</li>
    </ul>
  </div>
  <div class="col" style="left:600px">
    <h5>POPULAR PLACES</h5>
    <div class="places"><span>Florida</span><span>St Louis</span><span>New York</span><span style="color:var(--gold)">Jacksonville</span><span>Washington</span><span>San Jose</span><span>Los Angeles</span><span>San Diego</span><span>Chicago</span><span>Houston</span></div>
  </div>
  <div class="col" style="left:880px;width:280px;text-align:center">
    <h5>NEWSLETTER</h5>
    <p>Subscribe your email to get the latest news and new offer about discount</p>
    <div class="news-input"><span>Email Address</span><b></b></div>
  </div>
  <div class="abs copy">Copyright ©2018 All rights reserved</div>
</footer>

</body>
</html>
```